Etiketten-Design für Wein
Zielgruppe
Wir produzieren Wein und sind auf der Suche nach einer innovativen Weinetikette, welche sich durch unsere Weinvariationen durchziehen lässt.
Für das stehen wir ein: Nachhaltigkeit, moderne Landwirtschaft, Familienbetrieb, zukunftsorientiert, im Einklang mi der Natur, Freude an Pflanzen und Tieren.
Was uns gefällt: Relief / Prägung, eher schlichte, moderne und edle Etiketten, allenfalls Elemente aus der Natur, die auf Nachhaltigkeit hinweisen
Das möchten wir nicht auf der Etikette: zu knallige Farben, Comicfiguren oder ähnliches.
Unsere Weine werden direkt vermarktet und sollen aufgrund ihrer Etikette aus dem Weinregal herausstechen und ein Eyecatcher für die Kund:innen sein. Auch in einem Restaurant sollen sie als edlen Wein präsentiert werden können. Wir möchten, dass die Weinetiketten ein Storytelling mit sich bringen in Bezug auf die obenstehenden Punkte, für die wir einstehen.
Unsere Zielgruppe: Qualitätsbewusste Weingeniesser, mittleren und jüngeren Alters
Aufgabenstellung
Folgende Angaben sind auf der Etikette erforderlich:
- Weinsorte: Reserva / Riesling / Blauburgunder / Federweisser
- Name: Sennbachgut (kann klein und schlicht, unauffällig sein)
Unser Logo kann in Etikette aufgegriffen werden (auch in angepasster Form), ist aber nicht zwingend nötig. Das Logo ist auch eher revisionsbedürftig. ????
Folgende Masse sollte die Etikette ca. haben:
- Breite 95 mm
- Höhe 80 mm

```html
<!DOCTYPE html>
<html lang="de">
<head>
<meta charset="utf-8">
<title>Sennbachgut Riesling – Etikette</title>
<link rel="stylesheet" href="https://fonts.googleapis.com/css2?family=IBM+Plex+Mono:wght@400&family=Playfair+Display:wght@700&family=Zilla+Slab:wght@500&display=swap">
<style>
  :root {
    --page: #e6e6e4;
    --label: #f3f3f2;
    --label-edge: #e9e9e8;
    --ink: #1b1b1b;
    --leaf: #cbbda3;
  }
  * { margin: 0; padding: 0; box-sizing: border-box; }
  html, body {
    width: 1200px;
    height: 1200px;
    overflow: hidden;
    background: var(--page);
  }
  .label {
    position: absolute;
    left: 100px;
    top: 190px;
    width: 1000px;
    height: 820px;
    background: linear-gradient(90deg, var(--label-edge) 0%, var(--label) 12%, var(--label) 88%, var(--label-edge) 100%);
    box-shadow: 0 2px 12px rgba(0,0,0,0.08);
  }
  .label__leaf {
    position: absolute;
    left: 184px;
    top: 196px;
    width: 637px;
    height: 563px;
  }
  .label__place {
    position: absolute;
    top: 68px;
    width: 100%;
    text-align: center;
    font-family: "IBM Plex Mono", monospace;
    font-size: 29px;
    letter-spacing: 0.2em;
    color: var(--ink);
  }
  .label__estate {
    position: absolute;
    top: 122px;
    width: 100%;
    text-align: center;
    font-family: "Playfair Display", serif;
    font-weight: 700;
    font-size: 44px;
    letter-spacing: 0.08em;
    text-transform: uppercase;
    color: var(--ink);
  }
  .label__variety {
    position: absolute;
    top: 346px;
    width: 100%;
    text-align: center;
    font-family: "Zilla Slab", serif;
    font-weight: 500;
    font-size: 124px;
    line-height: 1;
    letter-spacing: 0.1em;
    padding-left: 0.1em;
    color: var(--ink);
  }
  .label__vintage {
    position: absolute;
    top: 656px;
    width: 100%;
    text-align: center;
    font-family: "IBM Plex Mono", monospace;
    font-size: 34px;
    letter-spacing: 0.2em;
    padding-left: 0.2em;
    color: var(--ink);
  }
</style>
</head>
<body>
  <main class="label">
    <svg class="label__leaf" viewBox="0 0 637 563" role="img" aria-label="Gestempeltes Rebblatt in Beige als Hintergrundmotiv">
      <ellipse cx="318" cy="282" rx="300" ry="270" fill="var(--leaf)"/>
    </svg>
    <p class="label__place">REBMATT</p>
    <h1 class="label__estate">Sennbachgut</h1>
    <h2 class="label__variety">RIESLING</h2>
    <p class="label__vintage">2023</p>
  </main>
</body>
</html>
```